Header Card Design for Marine Tool Product

We package up our small tools in bags. A nice header card would finish the look.
* Bag is 4" wide. Header Card should be 4x4, folded to 4x2
* Back of card should have 2.25x1.25 area for our part number sticker.
* Design to reinforce the brand and add (perception of) quality to the product.

Brand Website: harbolwex.com

Target Market(s)

Boat Mechanics/Boat owners

Industry/Entity Type

```html
<!DOCTYPE html>
<html lang="en">
<head>
<meta charset="utf-8">
<title>Harbolwex Header Card</title>
<link rel="stylesheet" href="https://fonts.googleapis.com/css2?family=Montserrat:wght@800&family=Oswald:wght@500&family=Roboto+Condensed:wght@400;700&display=swap">
<style>
  :root {
    --navy: #022a3f;
    --navy-soft: #0d3a57;
    --white: #ffffff;
    --paper: #ffffff;
    --ink: #111111;
    --frame: #b5b5b5;
  }
  html, body { margin: 0; padding: 0; overflow: hidden; }
  body { width: 1155px; height: 1200px; background: var(--paper); }
  .sheet {
    position: relative; width: 1155px; height: 1200px;
    box-sizing: border-box; border: 1px solid var(--frame); overflow: hidden;
  }
  .side-label {
    position: absolute; left: 0; width: 100%; text-align: center;
    font-family: Arial, Helvetica, sans-serif; font-size: 27px; color: var(--ink);
  }
  .side-label--back { top: 90px; transform: rotate(180deg); }
  .side-label--front { top: 1080px; }

  .panel {
    position: absolute; left: 112px; width: 931px; height: 465px;
    background: var(--navy); color: var(--white); overflow: hidden;
  }
  .panel--back { top: 132px; transform: rotate(180deg); }
  .panel--front { top: 598px; }
  .fold-line {
    position: absolute; left: 112px; top: 597px; width: 931px; height: 1px; background: var(--white);
  }

  .hang-hole { position: absolute; left: 374px; top: 44px; width: 184px; height: 64px; }

  .brand-name {
    position: absolute; font-family: "Montserrat", sans-serif; font-weight: 800;
    color: var(--white); white-space: nowrap; line-height: 1;
  }

  /* back */
  .panel--back .brand-name { left: 37px; top: 240px; font-size: 40px; letter-spacing: 1px; }
  .address {
    position: absolute; left: 37px; top: 318px; margin: 0;
    font-family: "Roboto Condensed", sans-serif; font-size: 28px; line-height: 32px;
  }
  .phone {
    position: absolute; left: 37px; top: 392px; display: flex; align-items: center; gap: 16px;
    font-family: "Roboto Condensed", sans-serif; font-size: 28px; letter-spacing: 6px;
  }
  .phone-icon { width: 36px; height: 36px; }
  .website {
    position: absolute; left: 638px; top: 50px;
    font-family: "Roboto Condensed", sans-serif; font-weight: 700; font-size: 27px; letter-spacing: 1px;
  }
  .sticker-area {
    position: absolute; left: 372px; top: 138px; width: 521px; height: 288px;
    box-sizing: border-box; border: 3px solid var(--white); border-radius: 12px;
  }

  /* front */
  .panel--front .brand-name { left: 253px; top: 200px; font-size: 56px; letter-spacing: 1px; }
  .tagline {
    position: absolute; left: 253px; top: 344px;
    font-family: "Oswald", sans-serif; font-weight: 500; font-size: 29px; letter-spacing: .3px;
    white-space: nowrap;
  }
  .gear-art {
    position: absolute; left: 679px; top: 67px; width: 214px; height: 214px;
    border-radius: 50%; border: 2px solid var(--white); box-sizing: border-box;
    background: radial-gradient(circle, var(--navy-soft), var(--navy));
  }
  .gear-art--faint {
    left: 824px; top: 45px; width: 140px; height: 140px; border: 1px solid var(--navy-soft);
    background: var(--navy-soft); opacity: .55;
  }
  .gear-art--faint-low {
    left: 708px; top: 215px; width: 300px; height: 300px; border: 1px solid var(--navy-soft);
    background: var(--navy-soft); opacity: .4;
  }
</style>
</head>
<body>
<div class="sheet">
  <div class="side-label side-label--back">BACK</div>

  <section class="panel panel--back" aria-label="Back of header card">
    <svg class="hang-hole" viewBox="0 0 184 64" aria-hidden="true">
      <path d="M20,22 H62 Q66,22 68,18 A27,27 0 0 1 116,18 Q118,22 122,22 H162 A20,20 0 0 1 162,62 H20 A20,20 0 0 1 20,22 Z" fill="none" stroke="#fff" stroke-width="3"/>
    </svg>
    <div class="website">www.harbolwex.com</div>
    <div class="sticker-area" aria-label="Part number sticker area"></div>
    <div class="brand-name">HARBOLWEX</div>
    <p class="address">418 Tidewater Ave, Suite 12<br>Port Avery&nbsp;&nbsp; SC,&nbsp;&nbsp; 29000</p>
    <div class="phone">
      <svg class="phone-icon" viewBox="0 0 36 36" aria-hidden="true">
        <circle cx="18" cy="18" r="18" fill="#fff"/>
        <path d="M13 9 h4 l1 6 -3 2 q2 4 5 6 l2 -3 6 1 v4 q-1 3 -4 3 q-12 -2 -15 -15 q0 -3 4 -4z" fill="#022a3f"/>
      </svg>
      <span>(555) 014-2290</span>
    </div>
  </section>

  <div class="fold-line" aria-hidden="true"></div>

  <section class="panel panel--front" aria-label="Front of header card">
    <div class="gear-art gear-art--faint" role="img" aria-label="Faint gear outline decoration"></div>
    <div class="gear-art gear-art--faint-low" role="img" aria-label="Faint gear outline decoration"></div>
    <div class="gear-art" role="img" aria-label="Line drawing of a gear inside a circle"></div>
    <svg class="hang-hole" viewBox="0 0 184 64" aria-hidden="true">
      <path d="M20,22 H62 Q66,22 68,18 A27,27 0 0 1 116,18 Q118,22 122,22 H162 A20,20 0 0 1 162,62 H20 A20,20 0 0 1 20,22 Z" fill="none" stroke="#fff" stroke-width="3"/>
    </svg>
    <div class="brand-name">HARBOLWEX</div>
    <div class="tagline">Born in Port Avery, South Carolina</div>
  </section>

  <div class="side-label side-label--front">FRONT</div>
</div>
</body>
</html>
```